Reverse Mortgage company needs a Facebook design

We need a facebook design for a mortgage company based in Orange County California. I started the facebook page at https://www.examplesocial.test/Tidewaterlendingandtrust. We specialize in mortgage financing and our main focus is Reverse Mortgages. We would like to see a design that would incorporate our existing color scheme on the loanbridgeready.test website. The design should be tailored for homeowners 62 years of age and older.
Updates
The DUNE inc jpg file that I uploaded is the logo that we use. The 2nd jpg that I uploaded was just to give you a better image of the graphic. Thank you
Target Market(s)
American Homeowners age 62 and older
Industry/Entity Type
It Company
Colors
Designer to choose colors to be used in the design.
Look and feel
Each slider illustrates characteristics of the customer's brand and the style your logo design should communicate.

```html
<!DOCTYPE html>
<html lang="en">
<head>
<meta charset="utf-8">
<title>DUNE inc – Facebook Cover</title>
<link rel="stylesheet" href="https://fonts.googleapis.com/css2?family=Montserrat:wght@500;800&family=Open+Sans:wght@600&display=swap">
<style>
  :root {
    --stage-deep: #0b0f4f;
    --stage-light: #4a4f9a;
    --cover-white: #ffffff;
    --ink: #111111;
    --brand-green: #6aab1f;
    --brand-navy: #2b2e6b;
    --placeholder-grey: #c2c2c2;
    --badge-gold: #f2a81d;
    --badge-rim: #1c1c1c;
  }
  * { margin: 0; padding: 0; box-sizing: border-box; }
  html, body { width: 1200px; height: 573px; overflow: hidden; }
  body {
    position: relative;
    background: radial-gradient(ellipse at 50% 25%, var(--stage-light) 0%, #262a7a 45%, var(--stage-deep) 100%);
    font-family: "Open Sans", Arial, sans-serif;
  }
  .cover {
    position: absolute;
    left: 95px; top: 80px;
    width: 1026px; height: 379px;
    background: var(--cover-white);
    overflow: hidden;
  }
  .cover-photo {
    position: absolute;
    left: 420px; top: 0;
    width: 606px; height: 379px;
    background:
      linear-gradient(90deg, var(--cover-white) 0%, rgba(255,255,255,0.6) 22%, rgba(255,255,255,0) 45%),
      linear-gradient(180deg, #e9e4dc 0%, #d8cfc2 40%, #5f7fc4 70%, #4a6fc0 100%);
  }
  .brand {
    position: absolute;
    left: 45px; top: 30px;
  }
  .brand-name {
    font-family: "Montserrat", Arial, sans-serif;
    font-weight: 800;
    font-size: 104px;
    line-height: 1;
    letter-spacing: 1px;
    color: var(--ink);
  }
  .brand-tagline {
    margin-top: 10px;
    font-family: "Montserrat", Arial, sans-serif;
    font-weight: 500;
    font-size: 23px;
    color: var(--brand-green);
  }
  .guarantee-seal {
    position: absolute;
    left: 910px; top: 10px;
  }
  .benefits {
    position: absolute;
    left: 405px; top: 256px;
    width: 621px;
    list-style: none;
  }
  .benefit {
    display: flex;
    align-items: center;
    height: 39px;
    margin-bottom: 13px;
    padding-left: 72px;
    background: var(--cover-white);
    font-weight: 600;
    font-size: 19px;
  }
  .benefit svg { margin-right: 14px; flex: none; }
  .benefit--green { color: var(--brand-green); }
  .benefit--navy { color: var(--brand-navy); }
  .profile-slot {
    position: absolute;
    left: 153px; top: 318px;
    width: 161px; height: 162px;
    background: var(--placeholder-grey);
    display: flex; align-items: center; justify-content: center;
    color: var(--cover-white);
    font-weight: 600;
    font-size: 18px;
  }
</style>
</head>
<body>
  <section class="cover">
    <div class="cover-photo" role="img" aria-label="Photo of a smiling senior couple standing in front of their home's white front door"></div>

    <div class="brand">
      <div class="brand-name">DUNE inc</div>
      <div class="brand-tagline">Tidewater Lending and Trust.com</div>
    </div>

    <svg class="guarantee-seal" width="92" height="92" viewBox="0 0 92 92" aria-hidden="true">
      <circle cx="46" cy="46" r="45" fill="var(--badge-rim)"/>
      <circle cx="46" cy="46" r="39" fill="var(--badge-gold)"/>
    </svg>

    <ul class="benefits">
      <li class="benefit benefit--green">
        <svg width="36" height="28" viewBox="0 0 36 28" aria-hidden="true">
          <path d="M2 15 L13 25 L34 3" fill="none" stroke="var(--brand-green)" stroke-width="6" stroke-linecap="round" stroke-linejoin="round"/>
        </svg>
        Best rated mortgage company in Orange County
      </li>
      <li class="benefit benefit--navy">
        <svg width="36" height="28" viewBox="0 0 36 28" aria-hidden="true">
          <path d="M2 15 L13 25 L34 3" fill="none" stroke="var(--brand-navy)" stroke-width="6" stroke-linecap="round" stroke-linejoin="round"/>
        </svg>
        Special rates for our clients over 60 years of age
      </li>
    </ul>
  </section>

  <div class="profile-slot">logo here</div>
</body>
</html>
```